Granite Ridge Response Business Card

Side 1: Granite Ridge Response Logo (logo without Maltese cross) with industrial rope rescue related theme. Our company services - TRAINING - Fire Training, Confined Space Rescue Training, Rope Rescue training, Hazmat Training, Incident Command, EMS, Pump Operations Training. Website - graniteridgeresponse.example.
Side 2: Granite Ridge Response Fire Department Logo (logo with Maltese cross) with Firefighter related theme. Company (division) services - FIELD SERVICES - Fire Department, Stand-by Rescue, Safety, EMS, Planning. "Supporting the Emergency Response Community Since 1967"

Add contact information wherever it makes since (Name, Email, Phone).
I would like it to represent the Granite Ridge Response Fire Department Logo as a division not as a separate entity without saying it, possibly by depicting it in the background of Side 2 instead of being a standalone picture like the logo on Side 1.

```html
<!DOCTYPE html>
<html lang="en">
<head>
<meta charset="utf-8">
<title>Granite Ridge Response Business Card</title>
<link href="https://fonts.googleapis.com/css2?family=Poppins:wght@400;500;700;800&display=swap" rel="stylesheet">
<style>
  :root {
    --stage: #1c1c1c;
    --paper: #ffffff;
    --red: #ff0000;
    --red-soft: rgba(255, 255, 255, 0.16);
    --graphite: #3c3c3e;
    --ink: #1f1f1f;
    --white: #ffffff;
  }
  * { margin: 0; padding: 0; box-sizing: border-box; }
  html, body {
    width: 1200px; height: 1015px; overflow: hidden;
    background: var(--stage);
    font-family: "Poppins", sans-serif;
  }
  .stage {
    position: relative; width: 1200px; height: 1015px;
    display: flex; flex-direction: column; align-items: center; justify-content: center; gap: 44px;
  }
  .card {
    position: relative; width: 760px; height: 434px; overflow: hidden;
    box-shadow: 0 18px 40px rgba(0, 0, 0, 0.55);
  }

  /* Side 1 */
  .card--front { background: var(--paper); }
  .service-list {
    position: absolute; left: 56px; top: 92px; list-style: none;
    font-size: 21px; line-height: 27px; color: var(--ink); font-weight: 400;
  }
  .service-list li { position: relative; padding-left: 22px; }
  .service-list li::before {
    content: ""; position: absolute; left: 2px; top: 11px;
    width: 9px; height: 9px; border-radius: 50%; background: var(--red);
  }
  .brand-lockup {
    position: absolute; right: 48px; top: 84px; width: 270px;
    display: flex; align-items: center; gap: 14px;
  }
  .brand-lockup .brand-dot {
    flex: none; width: 40px; height: 40px; border-radius: 50%; background: var(--red);
  }
  .brand-lockup .brand-name {
    font-size: 28px; line-height: 32px; font-weight: 800; color: var(--red);
    text-transform: uppercase;
  }
  .footer-band {
    position: absolute; left: 0; right: 0; bottom: 0; height: 78px;
  }
  .footer-band .band-graphite {
    position: absolute; left: 0; bottom: 0; width: 230px; height: 78px; background: var(--graphite);
  }
  .footer-band .band-red {
    position: absolute; left: 230px; right: 0; bottom: 0; height: 78px; background: var(--red);
    display: flex; align-items: center; justify-content: center;
  }
  .footer-band .website { color: var(--white); font-size: 19px; font-weight: 500; letter-spacing: 0.3px; }
  .footer-band .band-mark {
    position: absolute; left: 180px; top: 50%; transform: translateY(-50%);
    width: 64px; height: 64px; border-radius: 50%; background: var(--paper);
  }

  /* Side 2 */
  .card--back { background: var(--red); color: var(--white); }
  .division-watermark {
    position: absolute; right: -40px; top: -30px; width: 420px; height: 420px;
    border-radius: 50%; border: 10px solid var(--red-soft);
    display: flex; align-items: center; justify-content: center; text-align: center;
  }
  .division-watermark span {
    font-size: 46px; line-height: 52px; font-weight: 800; color: var(--red-soft);
    text-transform: uppercase; width: 300px;
  }
  .contact {
    position: absolute; left: 54px; top: 52px;
  }
  .contact .person { font-size: 30px; font-weight: 800; line-height: 38px; }
  .contact .detail {
    display: flex; align-items: center; gap: 10px;
    font-size: 19px; line-height: 27px; font-weight: 400;
  }
  .contact .detail svg { width: 17px; height: 17px; flex: none; }
  .rule { width: 140px; height: 1px; background: rgba(255, 255, 255, 0.75); margin: 16px 0 12px; }
  .field-list { list-style: none; font-size: 21px; line-height: 26px; }
  .field-list li { position: relative; padding-left: 20px; }
  .field-list li::before {
    content: ""; position: absolute; left: 2px; top: 11px;
    width: 8px; height: 8px; border-radius: 50%; background: var(--white);
  }
  .tagline { font-size: 18px; font-weight: 500; letter-spacing: 0.2px; }
</style>
</head>
<body>
<main class="stage">

  <section class="card card--front" aria-label="Granite Ridge Response, training side">
    <ul class="service-list">
      <li>Fire Training</li>
      <li>Confined Space Rescue Training</li>
      <li>Rope Rescue training</li>
      <li>Hazmat Training</li>
      <li>Incident Command</li>
      <li>EMS</li>
      <li>Pump Operations Training</li>
    </ul>

    <div class="brand-lockup">
      <span class="brand-dot"></span>
      <span class="brand-name">Granite Ridge Response</span>
    </div>

    <div class="footer-band">
      <div class="band-graphite"></div>
      <div class="band-red"><span class="website">www.graniteridgeresponse.example</span></div>
      <span class="band-mark"></span>
    </div>
  </section>

  <section class="card card--back" aria-label="Granite Ridge Response Fire Department, field services side">
    <div class="division-watermark"><span>Granite Ridge Response</span></div>

    <div class="contact">
      <p class="person">Marcus Delaney</p>
      <p class="detail">
        <svg viewBox="0 0 24 24" aria-hidden="true"><path fill="#fff" d="M6.6 10.8a15.5 15.5 0 0 0 6.6 6.6l2.2-2.2c.3-.3.7-.4 1-.2 1.1.4 2.3.6 3.6.6.6 0 1 .4 1 1V20c0 .6-.4 1-1 1A17 17 0 0 1 3 4c0-.6.4-1 1-1h3.5c.6 0 1 .4 1 1 0 1.3.2 2.5.6 3.6.1.3 0 .7-.2 1z"/></svg>
        555-014 220 381
      </p>
      <p class="detail">
        <svg viewBox="0 0 24 24" aria-hidden="true"><path fill="#fff" d="M2 5h20v14H2zm2 2v.5l8 5 8-5V7zm0 2.9V17h16V9.9l-8 5z"/></svg>
        contact@graniteridge.example
      </p>
      <div class="rule"></div>
      <ul class="field-list">
        <li>Fire Department</li>
        <li>Stand-by Rescue</li>
        <li>Safety</li>
        <li>EMS</li>
        <li>Planning</li>
      </ul>
      <div class="rule"></div>
      <p class="tagline">Supporting the Emergency Response Community Since 1967</p>
    </div>
  </section>

</main>
</body>
</html>
```